Valdoro Global Journeys Facebook Page

I would like to have a very professional and unique Facebook page for my business
www.valdoroglobaljourneys.com

```html
<!DOCTYPE html>
<html lang="en">
<head>
<meta charset="utf-8">
<title>Valdoro Global Journeys – Facebook Cover</title>
<link rel="stylesheet" href="https://fonts.googleapis.com/css2?family=Montserrat:wght@700&family=Oswald:wght@500&family=Open+Sans:wght@400;700&display=swap">
<style>
  :root {
    --teal: #23808a;
    --canvas: #e8e8e8;
    --white: #ffffff;
    --profile: #353535;
    --name-grey: #545454;
    --url-ink: #2c2c2c;
  }
  * { margin: 0; padding: 0; box-sizing: border-box; }
  html, body { width: 1200px; height: 1200px; overflow: hidden; background: var(--canvas); }
  .canvas { position: relative; width: 1200px; height: 1200px; }
  .cover {
    position: absolute; left: 50px; top: 353px;
    width: 1289px; height: 578px;
    transform: scale(0.8533); transform-origin: 0 0;
    background: var(--white);
  }
  .cover-art { position: absolute; inset: 0; }
  .headline {
    position: absolute; left: 0; top: 112px; width: 460px;
    text-align: center; color: var(--teal);
  }
  .headline-lead { font-family: "Montserrat", sans-serif; font-weight: 700; font-size: 38px; letter-spacing: 1.5px; line-height: 1.1; }
  .headline-main { font-family: "Montserrat", sans-serif; font-weight: 700; font-size: 60px; letter-spacing: 2px; line-height: 1.25; }
  .headline-sub { font-family: "Oswald", sans-serif; font-weight: 500; font-size: 37px; line-height: 1.2; transform: scaleX(0.88); }
  .profile-slot {
    position: absolute; left: 60px; top: 320px; width: 250px; height: 246px;
    background: var(--profile);
  }
  .page-name {
    position: absolute; left: 370px; top: 498px;
    font-family: "Open Sans", sans-serif; font-weight: 700; font-size: 35px; color: var(--name-grey);
  }
  .site-url {
    position: absolute; left: 610px; top: 450px;
    font-family: "Open Sans", sans-serif; font-weight: 400; font-size: 21px; color: var(--url-ink);
  }
  .brand {
    position: absolute; left: 968px; top: 22px;
    display: flex; align-items: center; gap: 12px;
    color: var(--teal); font-family: "Montserrat", sans-serif; font-weight: 700;
  }
  .brand-dot { width: 94px; height: 94px; border-radius: 50%; background: var(--teal); flex: none; }
  .brand-name { line-height: 1; }
  .brand-name-top { display: block; font-size: 38px; letter-spacing: 1px; }
  .brand-name-bottom { display: block; font-size: 15px; letter-spacing: 1.5px; margin-top: 6px; }
</style>
</head>
<body>
<div class="canvas">
  <section class="cover">
    <svg class="cover-art" width="1289" height="578" viewBox="0 0 1289 578" xmlns="http://www.w3.org/2000/svg">
      <defs>
        <linearGradient id="lakeTones" x1="0" y1="0" x2="0" y2="1">
          <stop offset="0" stop-color="#c7d2d6"/>
          <stop offset="0.22" stop-color="#e4d8cc"/>
          <stop offset="0.38" stop-color="#d9a688"/>
          <stop offset="0.52" stop-color="#5a5a72"/>
          <stop offset="0.64" stop-color="#2d3452"/>
          <stop offset="0.68" stop-color="#9fb0c2"/>
          <stop offset="0.84" stop-color="#c98f6c"/>
          <stop offset="1" stop-color="#6d6f80"/>
        </linearGradient>
      </defs>
      <g role="img" aria-label="Photo of snow-capped mountains at sunrise reflected in a calm lake">
        <polygon points="422,0 862,0 1122,478 412,478 546,230" fill="url(#lakeTones)"/>
        <polygon points="887,0 1289,0 1289,478 1147,478" fill="url(#lakeTones)"/>
      </g>
    </svg>

    <div class="headline">
      <p class="headline-lead">VISIT THE TOP OF</p>
      <p class="headline-main">THE WORLD</p>
      <p class="headline-sub">CHALLENGE YOURSELF</p>
    </div>

    <div class="brand">
      <span class="brand-dot"></span>
      <span class="brand-name">
        <span class="brand-name-top">VALDORO</span>
        <span class="brand-name-bottom">GLOBAL JOURNEYS</span>
      </span>
    </div>

    <p class="site-url">valdoroglobaljourneys.com</p>
    <div class="profile-slot"></div>
    <p class="page-name">Company Name</p>
  </section>
</div>
</body>
</html>
```